Asia based real estate financing firm needs and AWESOME design for a biz card -Harbor Lending Circle

Looking for a stylish, & corporate-looking business card for a real estate financing brokerage firm in Asia, offering global mortgage loans. I uploaded our current logos. We would like to add a splash of color (perhaps the house icon) or any other suggestions are open. For the winning designer, we have a lot of work! Thanks and best of luck!

Target Market(s)

Real estate investors globally. We want to look more like a BANK and NOT a real estate company. Please don't play up on a "house" design.

Industry/Entity Type

Banking

Contact Information for Business Card

Harbor Lending Circle
Peter Wilks
Co-Founder | Partner

14 Cassia Lane, Suite 310
Singapore 047219
www.hlc-example.asia
peterwilks@hlc-example.asia
+65 555-0142
WeChat: peterwilks

Colors

Designer to choose colors to be used in the design.

Requirements
Must have
• Must have the standard business requirements for a card; name, address, email, etc
• Can be horizontal or vertical.
Nice to have
• It would be great to see some sort of variation to the logo with a pop of color. Red is good as we're in Asia, however, other options work as well.
• Our tag line is - Borderless mortgages. It doesn't have to be on the card but might be nice.
• I'd like to start seeing our tagline within the cards as well. - Borderless mortgages.
• Also, please add our location. The location for this card is Singapore so perhaps it can be highlighted or emphasised in some way.
• Singapore | Hong Kong | Shanghai | Manila
• As we will soon open an office in Shanghai, having an option for both languages would be great.
Should not have
• I'm exceited and open to your creativity ... knock it out of the park!

```html
<!DOCTYPE html>
<html lang="en">
<head>
<meta charset="utf-8">
<title>Harbor Lending Circle – Business Card</title>
<link rel="stylesheet" href="https://fonts.googleapis.com/css2?family=Cinzel:wght@500&family=Montserrat:wght@400;600&display=swap">
<style>
  :root {
    --backdrop: #e8e6e3;
    --brand-red: #b01e24;
    --brand-red-dark: #7d1318;
    --ink: #0b0b0d;
    --paper: #ffffff;
    --text-light: #ffffff;
  }
  * { margin: 0; padding: 0; box-sizing: border-box; }
  html, body {
    width: 1200px; height: 891px; overflow: hidden;
    background: var(--backdrop);
  }
  .canvas {
    position: relative; width: 1200px; height: 891px;
    display: flex; align-items: center; justify-content: center; gap: 60px;
  }
  .card {
    position: relative; width: 520px; height: 297px; overflow: hidden;
    box-shadow: 0 6px 18px rgba(0,0,0,0.15);
  }
  /* Contact side */
  .card-back { background: var(--paper); }
  .card-back .shapes { position: absolute; inset: 0; }
  .wordmark-dark {
    position: absolute; left: 34px; top: 40px;
    display: flex; align-items: center; gap: 10px;
    font-family: "Cinzel", serif; font-weight: 500;
    font-size: 22px; letter-spacing: 1px; color: var(--ink);
  }
  .wordmark-dark .mark-square {
    width: 12px; height: 12px; background: var(--brand-red);
  }
  .name-band {
    position: absolute; left: 322px; top: 106px; width: 198px; height: 46px;
    color: var(--text-light); padding: 6px 0 0 14px;
    font-family: "Montserrat", sans-serif;
  }
  .name-band .person-name {
    font-size: 17px; font-weight: 600; letter-spacing: 1px; text-transform: uppercase;
  }
  .name-band .person-title {
    font-size: 8px; letter-spacing: 1px; text-transform: uppercase; margin-top: 2px;
  }
  .contact-list {
    position: absolute; left: 150px; top: 166px; list-style: none;
    font-family: "Montserrat", sans-serif; font-size: 12px; color: var(--text-light);
  }
  .contact-list li {
    display: flex; align-items: flex-start; gap: 8px; line-height: 15px; margin-bottom: 5px;
  }
  .contact-list svg { flex: none; width: 14px; height: 14px; margin-top: 0.5px; }

  /* Brand side */
  .card-front {
    background: var(--brand-red);
    display: flex; align-items: center; justify-content: center;
  }
  .wordmark-light {
    display: flex; align-items: center; gap: 12px;
    font-family: "Cinzel", serif; font-weight: 500;
    font-size: 28px; letter-spacing: 2px; color: var(--text-light);
  }
  .wordmark-light .mark-square {
    width: 14px; height: 14px; background: var(--text-light);
  }
</style>
</head>
<body>
<main class="canvas">

  <section class="card card-back" aria-label="Business card, contact side">
    <svg class="shapes" viewBox="0 0 520 297" width="520" height="297" aria-hidden="true">
      <polygon points="0,232 330,112 520,112 520,297 0,297" fill="var(--ink)"/>
      <polygon points="306,120 322,106 322,152 306,164" fill="var(--brand-red-dark)"/>
      <rect x="322" y="106" width="198" height="46" fill="var(--brand-red)"/>
    </svg>

    <div class="wordmark-dark"><span class="mark-square"></span>Harbor Lending Circle</div>

    <div class="name-band">
      <div class="person-name">Peter Wilks</div>
      <div class="person-title">Co-Founder | Partner</div>
    </div>

    <ul class="contact-list">
      <li>
        <svg viewBox="0 0 14 14"><circle cx="7" cy="7" r="7" fill="#fff"/><rect x="5" y="3" width="4" height="8" rx="1" fill="var(--ink)"/></svg>
        +65 555-0142
      </li>
      <li>
        <svg viewBox="0 0 14 14"><circle cx="7" cy="7" r="7" fill="#fff"/><ellipse cx="7" cy="6.5" rx="4" ry="3" fill="var(--ink)"/><polygon points="5,8 4,11 7,9" fill="var(--ink)"/></svg>
        peterwilks
      </li>
      <li>
        <svg viewBox="0 0 14 14"><circle cx="7" cy="7" r="7" fill="#fff"/><rect x="3.5" y="4.5" width="7" height="5" fill="var(--ink)"/><polyline points="3.5,4.5 7,7.5 10.5,4.5" fill="none" stroke="#fff" stroke-width="0.8"/></svg>
        peterwilks@hlc-example.asia
      </li>
      <li>
        <svg viewBox="0 0 14 14"><circle cx="7" cy="7" r="7" fill="#fff"/><circle cx="7" cy="7" r="4" fill="none" stroke="var(--ink)" stroke-width="1"/><line x1="3" y1="7" x2="11" y2="7" stroke="var(--ink)" stroke-width="0.8"/><ellipse cx="7" cy="7" rx="1.8" ry="4" fill="none" stroke="var(--ink)" stroke-width="0.8"/></svg>
        www.hlc-example.asia
      </li>
      <li>
        <svg viewBox="0 0 14 14"><circle cx="7" cy="7" r="7" fill="#fff"/><path d="M7 11.5 L4.3 7 A3 3 0 1 1 9.7 7 Z" fill="var(--ink)"/><circle cx="7" cy="5.8" r="1" fill="#fff"/></svg>
        <span>14 Cassia Lane, Suite 310<br>Singapore 047219</span>
      </li>
    </ul>
  </section>

  <section class="card card-front" aria-label="Business card, brand side">
    <div class="wordmark-light"><span class="mark-square"></span>Harbor Lending Circle</div>
  </section>

</main>
</body>
</html>
```